WordPress Website for Pain Relief Clinic

I need a WordPress website designed for my laser pain relief clinic. It needs to be a professional, responsive design with 7 pages: Home, Why Choose Us, Treatable Conditions, Testimonials, FAQ, Franchising, Contact Us. Here is logo: https://s3.cloudvexa-store.net/media.b-r-t-n.net/sitebuilder/361/KelvaroLogoHighQuality.png

Target Market(s)

people with pain,elderly adults,injuries,soreness

Industry/Entity Type

Clinic

Number of Pages Required

5+ page

Colors
0792cd
85abd2

```html
<!DOCTYPE html>
<html lang="en">
<head>
<meta charset="utf-8">
<title>Kelvaro Laser Pain Relief Clinic</title>
<link href="https://fonts.googleapis.com/css2?family=Open+Sans:wght@400;600;700;800&display=swap" rel="stylesheet">
<style>
:root{
  --blue:#0792cd;
  --blue-soft:#85abd2;
  --red:#e8363d;
  --ink:#333;
  --muted:#777;
  --line:#e3e3e3;
  --paper:#fff;
  --grey:#f3f3f3;
  --footer:#eeeeee;
}
*{box-sizing:border-box;margin:0;padding:0}
html,body{width:1200px;height:2880px;overflow:hidden;background:var(--paper)}
body{font-family:"Open Sans",Arial,sans-serif;color:var(--ink);font-size:13px;line-height:1.55}
.page{position:relative;width:1200px;height:2880px}
.abs{position:absolute}
.btn{display:inline-block;background:var(--red);color:#fff;font-size:11px;font-weight:700;padding:9px 18px;border-radius:3px;text-transform:uppercase}
.btn-blue{background:var(--blue);font-size:10px;padding:7px 14px}
.photo{background:linear-gradient(135deg,#d9c4b4,#b99a86)}

/* header */
.header{left:0;top:0;width:1200px;height:150px}
.brand{left:70px;top:30px;font-size:46px;font-weight:800;color:var(--blue);letter-spacing:-1px;line-height:1}
.brand-sub{left:72px;top:82px;font-size:11px;font-weight:700;color:var(--red);letter-spacing:3px}
.mail{left:650px;top:16px;font-size:11px;color:var(--muted)}
.mail b{display:block;color:var(--ink);font-size:11px}
.social{right:70px;top:18px;display:flex;gap:10px}
.social span{width:16px;height:16px;border-radius:50%;background:#aab}
.call{left:780px;top:58px;height:40px;display:flex;align-items:center}
.call .lbl{background:var(--red);color:#fff;font-size:13px;font-weight:700;height:40px;padding:0 16px;display:flex;align-items:center;gap:8px;text-transform:uppercase;white-space:nowrap}
.call .num{border:2px solid var(--red);height:40px;padding:0 16px;display:flex;align-items:center;font-size:26px;font-weight:800;color:var(--red);white-space:nowrap}
.nav{left:70px;top:124px;width:1060px;height:36px;background:var(--blue);display:flex;align-items:center}
.nav a{color:#fff;font-size:11px;font-weight:700;padding:0 16px;height:36px;display:flex;align-items:center;text-decoration:none;text-transform:uppercase;white-space:nowrap}
.nav a.on{background:var(--red)}
.search{margin-left:auto;margin-right:8px;width:170px;height:22px;background:#fff;font-size:10px;color:#999;padding:3px 8px}

/* hero */
.hero{left:70px;top:160px;width:1060px;height:488px}
.hero-copy{left:40px;top:80px;width:640px;color:#fff}
.hero-copy h1{font-weight:700;line-height:1.12;text-transform:uppercase}
.hero-copy h1 .l1{display:block;font-size:30px}
.hero-copy h1 .l2{display:block;font-size:44px;white-space:nowrap}
.hero-copy p{font-size:14px;width:440px;margin-top:16px}
.hero-copy .btn{margin-top:22px}
.dots{left:140px;bottom:16px;display:flex;gap:6px}
.dots i{width:8px;height:8px;border-radius:50%;background:#fff;opacity:.6}
.dots i:first-child{opacity:1}

/* welcome */
.welcome{left:70px;top:668px;width:640px}
.welcome h2{font-size:28px;font-weight:600;line-height:1.1}
.welcome h2 b{color:var(--blue)}
.welcome .tag{font-size:12px;color:var(--muted);margin-bottom:16px}
.welcome p{font-size:12px;color:var(--muted);margin-bottom:14px}
.panel{left:778px;top:615px;width:330px}
.panel .item{height:100px;background:var(--blue);color:#fff;display:flex;align-items:center;gap:18px;padding:0 20px;border-bottom:1px solid rgba(255,255,255,.3)}
.panel .item.red{background:var(--red)}
.panel .ico{width:46px;height:46px;border-radius:50%;border:2px solid #fff;flex:none;display:flex;align-items:center;justify-content:center}
.panel h4{font-size:15px;font-weight:700}
.panel .item p{font-size:11px;line-height:1.35}

/* services */
.services{left:0;top:1030px;width:1200px;height:480px;background:var(--grey)}
.sec-title{font-size:28px;font-weight:600;white-space:nowrap}
.sec-title b{color:var(--red)}
.rule{height:1px;background:#ccc}
.cards{left:70px;top:110px;display:flex;gap:22px}
.card{width:248px;background:#fff}
.card .photo{height:170px}
.card h5{font-size:12px;font-weight:700;padding:12px 14px 4px;text-transform:uppercase}
.card p{font-size:11px;color:var(--muted);padding:0 14px}
.card .btn{margin:10px 14px 16px}

/* appointment + doctor */
.appt{left:70px;top:1535px;width:320px;height:505px;border:1px solid var(--line)}
.appt .head{background:var(--blue);color:#fff;padding:16px 22px;height:100px}
.appt .head h3{font-size:22px;font-weight:600}
.appt .head .ph{font-size:18px;font-weight:700;display:flex;gap:8px;align-items:center}
.field{margin:0 22px 10px;height:30px;border:1px solid var(--line);font-size:11px;color:#999;padding:6px 10px}
.form{padding-top:18px}
.field.tall{height:66px}
.captcha{display:flex;gap:12px;margin:0 22px 12px;align-items:center}
.captcha .field{margin:0;width:130px}
.captcha span{font-style:italic;font-weight:700;font-size:16px;color:#555}
.doc{left:460px;top:1590px;width:300px}
.doc h3{font-size:20px;font-weight:700}
.doc .role{font-size:11px;color:var(--muted);margin-bottom:14px}
.doc p{font-size:12px;color:var(--muted);margin-bottom:14px}
.doc-photo{left:780px;top:1560px;width:350px;height:480px;background:linear-gradient(180deg,#e7eef4,#c6d6e4)}

/* why + patients */
.why{left:70px;top:2105px;width:420px}
.why h3,.say h3{font-size:28px;font-weight:600;margin-bottom:30px}
.why .row{display:flex;gap:16px;margin-bottom:24px}
.why .num{width:38px;height:38px;border-radius:50%;border:2px solid var(--blue);color:var(--blue);font-weight:700;display:flex;align-items:center;justify-content:center;flex:none}
.why .row p{font-size:11px;color:var(--muted)}
.why .row b{display:block;font-size:13px;color:var(--ink)}
.say{left:520px;top:2105px;width:610px}
.quote{display:flex;gap:24px;align-items:flex-start}
.avatar{width:90px;height:90px;border-radius:50%;flex:none;background:linear-gradient(135deg,#c7b3a4,#8d7565)}
.quote .txt{border-left:3px solid var(--line);padding-left:26px;font-size:12px;color:var(--muted);font-style:italic}
.quote .who{color:var(--red);font-style:normal;font-weight:600;margin-top:12px;font-size:11px}
.mark{font-size:60px;color:#ddd;line-height:.5;font-style:normal}

/* newsletter */
.news{left:0;top:2432px;width:1200px;height:72px;background:var(--red);color:#fff;display:flex;align-items:center;padding:0 70px}
.news h4{font-size:17px;font-weight:800;line-height:1.1;text-transform:uppercase;width:220px}
.news .in{width:250px;height:28px;background:#fff;color:#999;font-size:10px;padding:6px 10px;margin-left:50px}
.news .go{background:#222;color:#fff;font-size:10px;font-weight:700;padding:7px 14px;height:28px}
.news .stay{margin-left:auto;display:flex;gap:16px;align-items:center}
.news .stay span{width:24px;height:24px;border-radius:50%;background:rgba(255,255,255,.85)}

/* footer */
.footer{left:0;top:2504px;width:1200px;height:376px;background:var(--footer)}
.fcol{top:36px}
.fcol h6{font-size:12px;font-weight:700;text-transform:uppercase;margin-bottom:12px;padding-bottom:8px;border-bottom:1px solid #ccc}
.fcol p{font-size:11px;color:var(--muted);margin-bottom:10px}
.fbrand{left:920px;top:40px;font-size:40px;font-weight:800;color:var(--blue);letter-spacing:-1px;line-height:1}
.fsmall{left:920px;top:95px;width:210px;font-size:10px;color:var(--muted)}
</style>
</head>
<body>
<div class="page">

<header class="header abs">
  <div class="brand abs">Kelvaro</div>
  <div class="brand-sub abs">PAIN TREATMENT CENTER</div>
  <div class="mail abs"><b>EMAIL</b>info@kelvaroclinic.com</div>
  <div class="social abs"><span></span><span></span><span></span></div>
  <div class="call abs">
    <div class="lbl">
      <svg width="16" height="16" viewBox="0 0 24 24"><path fill="#fff" d="M6.6 10.8a15 15 0 006.6 6.6l2.2-2.2a1 1 0 011-.25 11.4 11.4 0 003.6.6 1 1 0 011 1V20a1 1 0 01-1 1A17 17 0 013 4a1 1 0 011-1h3.5a1 1 0 011 1c0 1.25.2 2.45.6 3.6a1 1 0 01-.25 1z"/></svg>
      Call Us Today Now!</div>
    <div class="num">555-210-4478</div>
  </div>
</header>

<nav class="nav abs">
  <a class="on">Home</a><a>Why Choose Us</a><a>Treatable Conditions</a><a>Testimonials</a><a>FAQ</a><a>Franchising</a><a>Contact</a>
  <div class="search">Enter Search</div>
</nav>

<section class="hero abs photo" role="img" aria-label="Photo of a runner holding a sore shoulder" style="background:linear-gradient(100deg,#4a5d6e 0%,#7d8f9b 45%,#c9a48e 100%)">
  <div class="hero-copy abs">
    <h1><span class="l1">Want relief from</span><span class="l2">Shoulder-pain? Tell us</span></h1>
    <p>In publishing and graphic design, lorem ipsum is a filler text commonly used to demonstrate the graphic elements of a document or visual presentation.</p>
    <span class="btn">Book an Appointment</span>
  </div>
  <div class="dots abs"><i></i><i></i><i></i><i></i><i></i></div>
</section>

<section class="welcome abs">
  <h2>Welcome to <b>Kelvaro</b></h2>
  <div class="tag">Laser Pain Relief Clinic</div>
  <p>Lorem ipsum is simply dummy text of the printing and typesetting industry. Lorem ipsum has been the industry's standard dummy text ever since the 1500s, when an unknown printer took a galley of type and scrambled it to make a type specimen book. It has survived not only five centuries, but also the leap into electronic typesetting, remaining essentially unchanged.</p>
  <p>When an unknown printer took a galley of type and scrambled it to make a type specimen book. It has survived not only five centuries, but also the leap into electronic typesetting unchanged.</p>
  <span class="btn btn-blue">Know More</span>
</section>

<aside class="panel abs">
  <div class="item"><div class="ico"><svg width="22" height="22" viewBox="0 0 24 24" fill="none" stroke="#fff" stroke-width="2"><rect x="3" y="5" width="18" height="16"/><path d="M3 10h18M8 3v4M16 3v4"/></svg></div><div><h4>Schedule An Appointment</h4><p>Lorem ipsum has been the industry's standard dummy text.</p></div></div>
  <div class="item red"><div class="ico"><svg width="22" height="22" viewBox="0 0 24 24" fill="none" stroke="#fff" stroke-width="2"><path d="M4 20V10l8-6 8 6v10zM10 20v-6h4v6"/></svg></div><div><h4>Our Franchising</h4><p>Lorem ipsum has been the industry's standard dummy text.</p></div></div>
  <div class="item"><div class="ico"><svg width="22" height="22" viewBox="0 0 24 24" fill="none" stroke="#fff" stroke-width="2"><circle cx="12" cy="12" r="9"/><path d="M12 7v6l4 2"/></svg></div><div><h4>What you can Expect?</h4><p>Lorem ipsum has been the industry's standard dummy text.</p></div></div>
  <div class="item"><div class="ico"><svg width="22" height="22" viewBox="0 0 24 24" fill="none" stroke="#fff" stroke-width="2"><circle cx="12" cy="8" r="4"/><path d="M4 21c1-5 15-5 16 0"/></svg></div><div><h4>Meet The Doctor</h4><p>Lorem ipsum has been the industry's standard dummy text.</p></div></div>
</aside>

<section class="services abs">
  <div class="abs" style="left:70px;top:32px;width:1060px;display:flex;align-items:center;gap:20px">
    <div class="sec-title">We Offer <b>Reliable Services</b></div><div class="rule" style="flex:1"></div>
  </div>
  <div class="cards abs">
    <div class="card"><div class="photo" role="img" aria-label="Photo of lower back pain"></div><h5>Back Pain</h5><p>In publishing and graphic design, lorem ipsum is a filler text commonly used.</p><span class="btn btn-blue">Know More</span></div>
    <div class="card"><div class="photo" role="img" aria-label="Photo of a sore knee" style="background:linear-gradient(135deg,#e2c9b8,#c79a82)"></div><h5>Knee Pain</h5><p>In publishing and graphic design, lorem ipsum is a filler text commonly used.</p><span class="btn btn-blue">Know More</span></div>
    <div class="card"><div class="photo" role="img" aria-label="Photo of shoulder pain" style="background:linear-gradient(135deg,#d8c2b2,#a77f6a)"></div><h5>Shoulder Pain</h5><p>In publishing and graphic design, lorem ipsum is a filler text commonly used.</p><span class="btn btn-blue">Know More</span></div>
    <div class="card"><div class="photo" role="img" aria-label="Photo of arm pain" style="background:linear-gradient(135deg,#e6d3c6,#b98d78)"></div><h5>Arm Pain</h5><p>In publishing and graphic design, lorem ipsum is a filler text commonly used.</p><span class="btn btn-blue">Know More</span></div>
  </div>
</section>

<section class="appt abs">
  <div class="head">
    <h3>Book an Appointment</h3>
    <div class="ph"><svg width="16" height="16" viewBox="0 0 24 24"><path fill="#fff" d="M6.6 10.8a15 15 0 006.6 6.6l2.2-2.2a1 1 0 011-.25 11.4 11.4 0 003.6.6 1 1 0 011 1V20a1 1 0 01-1 1A17 17 0 013 4a1 1 0 011-1h3.5a1 1 0 011 1c0 1.25.2 2.45.6 3.6a1 1 0 01-.25 1z"/></svg>555-210-4478</div>
  </div>
  <div class="form">
    <div class="field">Full Name</div>
    <div class="field">Phone Number</div>
    <div class="field">Email Address</div>
    <div class="field">Appointment Date</div>
    <div class="field tall">Message</div>
    <div class="captcha"><div class="field">Enter Code</div><span>zm8hx</span></div>
    <span class="btn" style="margin-left:22px">Submit Request</span>
  </div>
</section>

<section class="doc abs">
  <h3>Dr. Alan Weller</h3>
  <div class="role">MD, Kelvaro Laser Pain Relief Clinic</div>
  <p>In publishing and graphic design, lorem ipsum is a filler text commonly used to demonstrate the graphic elements of a document or visual presentation. Replacing meaningful content with placeholder text allows viewers to focus on graphic elements.</p>
  <p>In publishing and graphic design, lorem ipsum is a filler text commonly used to demonstrate the graphic elements of a document or visual presentation.</p>
  <span class="btn btn-blue">Know More</span>
</section>
<div class="doc-photo abs" role="img" aria-label="Photo of the clinic doctor in a white coat"></div>

<section class="why abs">
  <h3>Why Choose Us</h3>
  <div class="row"><div class="num">1</div><p><b>In Publishing and graphic design</b>In publishing and graphic design, lorem ipsum is a filler text.</p></div>
  <div class="row"><div class="num">2</div><p><b>In Publishing and graphic design</b>In publishing and graphic design, lorem ipsum is a filler text.</p></div>
  <div class="row"><div class="num">3</div><p><b>In Publishing and graphic design</b>In publishing and graphic design, lorem ipsum is a filler text.</p></div>
</section>

<section class="say abs">
  <h3>What Our Patients Say</h3>
  <div class="quote">
    <div class="avatar" role="img" aria-label="Portrait of a patient"></div>
    <div class="txt"><span class="mark">&ldquo;</span><br>In publishing and graphic design, lorem ipsum is a filler text commonly used to demonstrate the graphic elements of a document or visual presentation. Replacing meaningful content with placeholder text allows viewers to focus on graphic elements such as typeface and layout. The text is not meaningful and commonly used to demonstrate documents or visual presentation.
      <div class="who">&mdash; Mark Ellison</div></div>
  </div>
</section>

<section class="news abs">
  <h4>Subscribe<br>Our Newsletter</h4>
  <div class="in">Enter Your Email</div><div class="go">SUBSCRIBE</div>
  <div class="stay"><h4 style="width:auto">Stay<br>Connected</h4><span></span><span></span><span></span></div>
</section>

<footer class="footer abs">
  <div class="fcol abs" style="left:70px;width:240px">
    <h6>Recent Blog</h6>
    <p>10 March 2016 | 4 Comments<br>Sed ut perspiciatis unde omnis iste natus error sit.</p>
    <p>16 March 2016 | 2 Comments<br>Sed ut perspiciatis unde omnis iste natus error sit.</p>
  </div>
  <div class="fcol abs" style="left:360px;width:200px">
    <h6>Office Hours</h6>
    <p>Monday to Friday<br>9:00am - 6:00pm</p>
    <p>Saturday<br>9:00am - 3:00pm</p>
    <p>Sunday<br>Closed</p>
  </div>
  <div class="fcol abs" style="left:610px;width:240px">
    <h6>Get In Touch</h6>
    <p>120 Maple Avenue, Brookfield, ST 00000</p>
    <p>Phone:<br>555-210-4478</p>
    <p>Email:<br>info@kelvaroclinic.com</p>
  </div>
  <div class="fbrand abs">Kelvaro</div>
  <div class="fsmall abs">&copy; 2016 Kelvaro Laser Pain Relief Clinic. All Rights Reserved. Terms &amp; Conditions | Privacy Policy</div>
</footer>

</div>
</body>
</html>
```